Tolvane BrandWorks Corporate Site

Design a site to replace www.tolvanebrandworks.com, built for/within net harbor and incorporate numerous corporate assets and lines of business (www.pulsarstageworksinc.com, www.summitoutingpros.com, www.zapsnapkiosk.com, www.nibblecrate.com, www.strumbleorama.com) as well as our consulting and artist management work.

Target Market(s)

businesses, non profits, talent (performing artists)

Industry/Entity Type

Business

Coding

Coded - Design and coding required

Number of Pages Required

5+ page

Colors
0655a3
ffc214

Requirements
Must have
• social media visibility, multi-media

```html
<!DOCTYPE html>
<html lang="en">
<head>
<meta charset="utf-8">
<title>Tolvane BrandWorks</title>
<link rel="stylesheet" href="https://fonts.googleapis.com/css2?family=Jost:wght@600&family=Lato:wght@400;700&family=Raleway:wght@500&family=Source+Sans+3:wght@400&family=Tinos&display=swap">
<style>
  :root {
    --navy: #003a7b;
    --gold: #f0c35e;
    --ink: #1b1b1b;
    --charcoal: #222222;
    --muted: #8d8d8d;
    --white: #ffffff;
  }
  * { box-sizing: border-box; margin: 0; padding: 0; }
  html, body { width: 1200px; height: 1049px; overflow: hidden; }
  body { position: relative; background: var(--white); font-family: "Lato", sans-serif; }

  .site-header { position: absolute; top: 0; left: 0; width: 1200px; height: 115px; display: flex; align-items: center; justify-content: center; gap: 14px; }
  .brand-mark { width: 22px; height: 22px; background: var(--gold); }
  .brand-name { font-family: "Lato", sans-serif; font-weight: 700; font-size: 44px; color: var(--navy); letter-spacing: -0.5px; }

  .main-nav { position: absolute; top: 115px; left: 0; width: 1200px; height: 82px; background: var(--navy); }
  .main-nav a { position: absolute; top: 0; height: 82px; line-height: 82px; color: var(--white); text-decoration: none; font-size: 15.5px; transform: translateX(-50%); white-space: nowrap; }
  .main-nav a.is-active { left: 90px !important; width: 129px; transform: none; text-align: center; background: var(--gold); color: var(--ink); }

  .hero { position: absolute; top: 197px; left: 0; width: 1200px; height: 481px;
    background: linear-gradient(180deg, #1a1a1a 0%, #2d2c2a 28%, #3f3b36 50%, #5c564d 72%, #4a453e 88%, #3a3631 100%); }
  .hero-title { position: absolute; top: 92px; left: 200px; width: 800px; text-align: center; font-family: "Jost", sans-serif; font-weight: 600; font-size: 46px; line-height: 55px; color: var(--white); letter-spacing: 0.5px; text-shadow: 0 2px 6px rgba(0,0,0,.5); }
  .hero-intro { position: absolute; top: 224px; left: 210px; width: 780px; text-align: center; font-size: 17px; line-height: 22.7px; color: var(--white); text-shadow: 0 1px 4px rgba(0,0,0,.6); }
  .hero-button { position: absolute; top: 297px; left: 514px; width: 172px; height: 49px; line-height: 49px; text-align: center; background: var(--gold); color: var(--ink); font-size: 17px; text-decoration: none; }

  .services { position: absolute; top: 678px; left: 0; width: 1200px; height: 293px; background: var(--charcoal); border-top: 3px solid var(--white); }
  .service { position: absolute; top: -70px; width: 300px; margin-left: -150px; text-align: center; }
  .service-photo { width: 170px; height: 170px; margin: 0 auto; border-radius: 50%; border: 3px solid var(--white); }
  .service-title { margin-top: 27px; font-family: "Raleway", sans-serif; font-weight: 500; font-size: 16px; color: var(--white); }
  .service-text { margin: 8px auto 0; width: 230px; font-family: "Source Sans 3", sans-serif; font-size: 12.5px; line-height: 17px; color: var(--muted); }
  .service-more { display: inline-flex; align-items: center; gap: 6px; margin-top: 13px; font-size: 12.5px; color: var(--white); text-decoration: none; }

  .site-footer { position: absolute; top: 971px; left: 0; width: 1200px; height: 78px; background: var(--gold); }
  .copyright { position: absolute; top: 30px; left: 51px; font-family: "Tinos", serif; font-size: 12.5px; color: var(--ink); }
  .social { position: absolute; top: 32px; right: 52px; display: flex; gap: 24px; align-items: center; }
  .social-dot { width: 14px; height: 14px; border-radius: 50%; background: var(--navy); opacity: .8; }
</style>
</head>
<body>
  <header class="site-header">
    <span class="brand-mark"></span>
    <span class="brand-name">Tolvane BrandWorks</span>
  </header>

  <nav class="main-nav">
    <a class="is-active" href="#">HOME</a>
    <a href="#" style="left:281px">ABOUT</a>
    <a href="#" style="left:444px">OUR SERVICES</a>
    <a href="#" style="left:603px">CLIENTS</a>
    <a href="#" style="left:770px">NEWS &amp; EVENTS</a>
    <a href="#" style="left:926px">BLOG</a>
    <a href="#" style="left:1058px">CONTACT</a>
  </nav>

  <section class="hero" role="img" aria-label="Photo of a weathered wooden deck under soft blurred evening lights">
    <h1 class="hero-title">COMMUNICATE * COLLABORATE * CELEBRATE</h1>
    <p class="hero-intro">Is your marketing and communications partner responsive, and flexible?&nbsp; Creative, yet practical? Do they understand your business enough to be strategic? Do they care enough to be passionate?&nbsp; Your business deserves no less.&nbsp; In fact, it deserves much more.</p>
    <a class="hero-button" href="#">READ MORE</a>
  </section>

  <section class="services">
    <article class="service" style="left:249px">
      <div class="service-photo" role="img" aria-label="Photo of business people in silhouette meeting" style="background:radial-gradient(circle at 50% 40%, #f4f4f4 0%, #d8d8d8 55%, #3a3a3a 100%)"></div>
      <h2 class="service-title">PUBLIC RELATIONS</h2>
      <p class="service-text">Lorem ipsum dolor sit amet, consectetur ipsum dolor sit amet, consectetur adipis do edit</p>
      <a class="service-more" href="#">MORE <svg width="5" height="8" viewBox="0 0 5 8"><path d="M0 0L5 4L0 8Z" fill="#fff"/></svg></a>
    </article>
    <article class="service" style="left:605px">
      <div class="service-photo" role="img" aria-label="Photo of a hand holding a sphere of strategy words" style="background:radial-gradient(circle at 50% 45%, #ffffff 0%, #e6e6e6 50%, #9a8a80 100%)"></div>
      <h2 class="service-title">STRATEGIC MARKETING</h2>
      <p class="service-text">Lorem ipsum dolor sit amet, consectetur ipsum dolor sit amet, consectetur adipis do edit</p>
      <a class="service-more" href="#">MORE <svg width="5" height="8" viewBox="0 0 5 8"><path d="M0 0L5 4L0 8Z" fill="#fff"/></svg></a>
    </article>
    <article class="service" style="left:960px">
      <div class="service-photo" role="img" aria-label="Photo of many raised hands of different skin tones" style="background:radial-gradient(circle at 50% 60%, #d9a98a 0%, #b57a58 45%, #f2f2f2 100%)"></div>
      <h2 class="service-title">MULTICULTURAL MARKETING</h2>
      <p class="service-text">Lorem ipsum dolor sit amet, consectetur ipsum dolor sit amet, consectetur adipis do edit</p>
      <a class="service-more" href="#">MORE <svg width="5" height="8" viewBox="0 0 5 8"><path d="M0 0L5 4L0 8Z" fill="#fff"/></svg></a>
    </article>
  </section>

  <footer class="site-footer">
    <p class="copyright">All Rights Reserved. Copyrights @company Name. 2016</p>
    <div class="social">
      <svg width="14" height="14" viewBox="0 0 14 14" aria-label="RSS feed"><circle cx="2" cy="12" r="2" fill="#003a7b"/><path d="M0 6a8 8 0 0 1 8 8M0 1a13 13 0 0 1 13 13" fill="none" stroke="#003a7b" stroke-width="2"/></svg>
      <span class="social-dot" aria-label="Social network"></span>
      <span class="social-dot" aria-label="Social network"></span>
      <span class="social-dot" aria-label="Social network"></span>
      <span class="social-dot" aria-label="Social network"></span>
    </div>
  </footer>
</body>
</html>
```